Bus Card for Organic Hydroponic Produce company

We need a business card for a budding new business. We grow 100% organic, 100% hydroponic, 100% GMO free produce for sale in our local area. We need something bold and dynamic, not simple and elegant. We want to catch peoples attention and get them to visit our website to view more information about our products and services. Its difficult to explain on a business card the differences between our produce (tomatoes, cucumbers, peppers, etc...) and the kind they would buy at the local grocer or market. , so we need to push them to the website.
We have been brainstorming names for the company and have a few in mind, so choose whichever speaks most to your artistic flair and propose a card based on that one, or both. #1 "Marrowfield Organics" with a slogan something like....." When merely growing green merely isn't quite enough" OR #2 "Quillbrook Organics" with a slogan similar to...."The cutting edge in cleaner, purer organics" OR #3" "Tandrel Organics" with a slogan similar to: "Building a healthier future for those we leave behind"" OR #4 "Loamwise Path" with a slogan similar to: "Purity by Simplicity"
Eventually we will need assistance with web design, promotional and sales materials, etc. so if you offer those services, please indicate that with the design, though it is NOT necessary to offer any additional services to win this contest. WE will pick the winner solely on the business card we like the most.
We want something that stands out, and especially with the name "Oda's organics", we understand that a creative mind may wander into certain attention getting means that may not be quite within the realm of what we can hand out at our local grocer or farmers market. We definitely are not opposed to a little salacious undertone or allusion to attract attention, but please keep it tasteful if you skirt that grey area.
For our card, we use an online printer that can add foils, special die cuts, double sided cards, 3-d cards (we love these 32 pt cards), transparent or translucent cards and more. We love cards that have some of these things where possible and on all of our other business' cards we get rave reviews from customers about their uniqueness. plumtessa.com has the info on these accents if you wish to view what I am referencing.
So in conclusion, we want a unique, stylish, bold, vivid, 2 sided business card that will really stand out. Just usw a generic phone number and website for now and we will add them as they become available. Please email with any questions! Thanks in advance for your effort and creativity!
Target Market(s)
We are targeting parents who are conceintous of what their children and families are eating. Our target audience are moms, but we don't want to exclude anyone else who chooses to eat more healthy. Our target customer is the same customer that would shop at Brightcart stores or local farmers markets

```html
<!DOCTYPE html>
<html lang="en">
<head>
<meta charset="utf-8">
<title>Oda's organics – Business Card</title>
<link rel="stylesheet" href="https://fonts.googleapis.com/css2?family=Cabin:wght@400;700&family=Encode+Sans+Condensed:wght@400&display=swap">
<style>
  :root {
    --brand-green: #07805e;
    --leaf-green: #a8d080;
    --ink: #2a2a2a;
    --paper: #ffffff;
    --card-edge: #8a8a8a;
  }
  * { margin: 0; padding: 0; box-sizing: border-box; }
  html, body {
    width: 1200px; height: 900px; overflow: hidden;
    background: var(--paper);
    font-family: "Cabin", sans-serif;
    color: var(--ink);
  }
  .sheet { position: relative; width: 1200px; height: 900px; }

  .card { position: absolute; left: 220px; width: 758px; }
  .card--front { top: 3px; height: 427px; background: var(--brand-green); }
  .card--back { top: 468px; height: 427px; background: var(--paper); border: 1px solid var(--card-edge); }

  .wordmark {
    position: absolute;
    font-family: "Cabin", sans-serif; font-weight: 700;
    line-height: 0.88;
  }
  .wordmark__name { position: relative; display: inline-block; }
  .wordmark__dot { position: absolute; border-radius: 50%; background: var(--leaf-green); }

  .card--front .wordmark { left: 0; right: 0; top: 118px; text-align: center; color: var(--paper); font-size: 90px; }
  .card--front .wordmark__dot { width: 32px; height: 32px; right: -34px; top: 6px; }
  .card--back .wordmark { left: 54px; top: 46px; color: var(--brand-green); font-size: 58px; }
  .card--back .wordmark__dot { width: 21px; height: 21px; right: -26px; top: 4px; }

  .tagline { position: absolute; font-family: "Encode Sans Condensed", sans-serif; font-weight: 400; }
  .card--front .tagline { left: 0; right: 0; top: 296px; text-align: center; color: var(--paper); font-size: 20px; }
  .card--back .tagline { left: 53px; top: 185px; color: var(--brand-green); font-size: 15px; }

  .person { position: absolute; left: 405px; top: 108px; }
  .person__name { font-size: 32px; font-weight: 400; letter-spacing: 0.3px; line-height: 1.1; }
  .person__role { font-size: 22px; line-height: 1.2; }

  .contact { position: absolute; list-style: none; font-size: 21px; line-height: 1.35; }
  .contact li { position: relative; padding-left: 40px; margin-bottom: 6px; }
  .contact svg { position: absolute; left: 0; top: 2px; fill: var(--leaf-green); }
  .contact--place { left: 52px; top: 290px; }
  .contact--direct { left: 403px; top: 292px; }
  .contact--direct li { padding-left: 45px; margin-bottom: 6px; }
</style>
</head>
<body>
<main class="sheet">
  <section class="card card--front" aria-label="Card front">
    <div class="wordmark"><span class="wordmark__name">Oda's<br>organics<span class="wordmark__dot"></span></span></div>
    <p class="tagline">As fresh as if it were picked this dawn</p>
  </section>

  <section class="card card--back" aria-label="Card back">
    <div class="wordmark"><span class="wordmark__name">Oda's<br>organics<span class="wordmark__dot"></span></span></div>
    <p class="tagline">As fresh as if it were picked this dawn</p>

    <div class="person">
      <h1 class="person__name">ROWAN TILLERY</h1>
      <p class="person__role">Director</p>
    </div>

    <ul class="contact contact--place">
      <li>
        <svg width="22" height="38" viewBox="0 0 22 38" aria-hidden="true"><path d="M11 0C4.9 0 0 4.9 0 11c0 8 11 27 11 27s11-19 11-27C22 4.9 17.1 0 11 0zm0 15a4 4 0 1 1 0-8 4 4 0 0 1 0 8z"/></svg>
        48 Alder Lane,<br>Larkhaven, VA 20417
      </li>
      <li>
        <svg width="24" height="24" viewBox="0 0 24 24" aria-hidden="true"><path d="M12 1a11 11 0 1 0 0 22 11 11 0 0 0 0-22zm0 2c1.3 1.4 2.2 3.6 2.5 6h-5C9.8 6.6 10.7 4.4 12 3zm-2.7.5C8.6 5.1 8 7 7.6 9H3.5a9 9 0 0 1 5.8-5.5zm5.4 0A9 9 0 0 1 20.5 9h-4.1C16 7 15.4 5.1 14.7 3.5zM3.1 11h4.3v2H3.1a9 9 0 0 1 0-2zm6.4 0h5v2h-5zm7 0h4.4a9 9 0 0 1 0 2h-4.4zM3.5 15h4.1c.4 2 1 3.9 1.7 5.5A9 9 0 0 1 3.5 15zm6 0h5c-.3 2.4-1.2 4.6-2.5 6-1.3-1.4-2.2-3.6-2.5-6zm6.9 0h4.1a9 9 0 0 1-5.8 5.5c.7-1.6 1.3-3.5 1.7-5.5z"/></svg>
        www.OdasOrganics.com
      </li>
    </ul>

    <ul class="contact contact--direct">
      <li>
        <svg width="34" height="22" viewBox="0 0 34 22" aria-hidden="true"><path d="M17 0C8 0 1 3 0 7l1 4 8-2V5c5-1.5 11-1.5 16 0v4l8 2 1-4C33 3 26 0 17 0zM9 12l-2 10h20l-2-10zm8 2a3.5 3.5 0 1 1 0 7 3.5 3.5 0 0 1 0-7z"/></svg>
        555-555-5555
      </li>
      <li>
        <svg width="22" height="32" viewBox="0 0 22 32" aria-hidden="true"><path d="M4 0h14a4 4 0 0 1 4 4v24a4 4 0 0 1-4 4H4a4 4 0 0 1-4-4V4a4 4 0 0 1 4-4zm0 4v20h14V4zm7 22.5a2 2 0 1 0 0 .1z"/></svg>
        555-555-5555
      </li>
      <li>
        <svg width="32" height="22" viewBox="0 0 32 22" aria-hidden="true"><path d="M0 0h32v2L16 13 0 2zm0 5l11 8L0 22zm32 0v17L21 13zM13 14.5l3 2 3-2L31 22H1z"/></svg>
        Odasorganics@mailhollow.com
      </li>
    </ul>
  </section>
</main>
</body>
</html>
```